Tavo Payments Business card refresh

Need a new design of our business card The info is not what is on these cards i sent this for a reference. I can email all the info over
Info would be Derek Whitfield Chief TAVO is the title. our new address is 47615 Birch Hollow Rd. Cedar Grove Or 91384 Cell number is 805-634-2917 Work number is 855-482-7309 ext 212 Derek@tavopayments.com is my email address
Target Market(s)
Merchant Services all businesses that take credit cards
Industry/Entity Type
Merchant Services / Credit Card processing
Contact Information for Business Card
Need a new design of our business card The info is not what is on these cards i sent this for a reference. I can email all the info over Info would be Derek Whitfield Chief TAVO is the title. our new address is 47615 Birch Hollow Rd. Cedar Grove Or 91384 Cell number is 805-634-2917 Work number is 855-482-7309 ext 212 Derek@tavopayments.com is my email address
Requirements
Must have
- My logo and colors from my brand guidelines
Nice to have
- i sent some designs just need a new refresh
Should not have
- nothing specific

```html
<!DOCTYPE html>
<html lang="en">
<head>
<meta charset="utf-8">
<title>Tavo Payments – Business Card</title>
<link href="https://fonts.googleapis.com/css2?family=Montserrat:wght@400;500;600;700&display=swap" rel="stylesheet">
<style>
  :root {
    --stage: #3a3a3a;
    --card: #121212;
    --lime: #8dc21f;
    --white: #f2f2f2;
    --muted: #d8d8d8;
    --rule: #4a4a4a;
    --emboss: #222222;
  }
  * { box-sizing: border-box; margin: 0; padding: 0; }
  html, body {
    width: 1200px; height: 1200px; overflow: hidden;
    background: var(--stage);
    font-family: "Montserrat", sans-serif;
  }
  .stage {
    width: 1200px; height: 1200px;
    display: flex; flex-direction: column;
    align-items: center; justify-content: center; gap: 56px;
  }
  .card {
    position: relative;
    width: 820px; height: 469px;
    background: var(--card);
    border-radius: 34px;
    box-shadow: 0 3px 0 var(--lime), 0 14px 30px rgba(0,0,0,.45);
    overflow: hidden;
  }
  /* Front */
  .brand-name {
    position: absolute; left: 0; right: 0; top: 98px;
    text-align: center;
    font-weight: 700; font-size: 62px; letter-spacing: 3px;
    color: var(--white);
    white-space: nowrap;
  }
  .rule-main {
    position: absolute; left: 56px; right: 56px; top: 262px;
    height: 2px; background: var(--lime);
  }
  .person { position: absolute; left: 56px; top: 216px; }
  .person-name {
    font-weight: 700; font-size: 30px; color: var(--lime);
    text-transform: uppercase; letter-spacing: .5px;
  }
  .person-title {
    margin-top: 18px;
    font-weight: 500; font-size: 17px; color: var(--white);
    text-transform: uppercase; letter-spacing: .5px;
  }
  .person-title b { font-weight: 700; }
  .rule-short {
    position: absolute; left: 56px; top: 320px;
    width: 310px; height: 1px; background: var(--lime);
  }
  .divider {
    position: absolute; left: 420px; top: 288px;
    width: 1px; height: 90px; background: var(--rule);
  }
  .contact-list { position: absolute; list-style: none; }
  .contact-list.phones { left: 56px; top: 340px; }
  .contact-list.reach { left: 452px; top: 288px; }
  .contact-list li {
    display: flex; align-items: flex-start; gap: 12px;
    font-size: 19px; line-height: 1.3; color: var(--muted);
    margin-bottom: 8px;
    white-space: nowrap;
  }
  .contact-list svg { flex: none; width: 20px; height: 22px; margin-top: 2px; }
  /* Back */
  .brand-name.faint {
    top: 50%; transform: translateY(-50%);
    font-size: 80px; letter-spacing: 2px; color: var(--emboss);
  }
</style>
</head>
<body>
<main class="stage">
  <section class="card card-front" aria-label="Business card front">
    <div class="brand-name">Tavo Payments</div>
    <div class="rule-main"></div>
    <div class="person">
      <div class="person-name">Derek Whitfield</div>
      <div class="person-title">Chief <b>TAVO</b></div>
    </div>
    <div class="rule-short"></div>
    <ul class="contact-list phones">
      <li>
        <svg viewBox="0 0 20 22" aria-hidden="true"><rect x="5" y="1" width="10" height="20" rx="2" fill="none" stroke="#8dc21f" stroke-width="1.6"/><circle cx="10" cy="17.5" r="1" fill="#8dc21f"/></svg>
        805-634-2917
      </li>
      <li>
        <svg viewBox="0 0 20 22" aria-hidden="true"><path d="M4 3c1.5-1 3 0 3.5 1.5l1 2.5c.3 1-.2 1.8-1 2.4 1 2.2 2.6 3.8 4.8 4.8.6-.8 1.4-1.3 2.4-1l2.5 1c1.5.5 2.5 2 1.5 3.5-1 1.6-3 2.2-5 1.5C8.5 17.5 4.5 13.5 2.8 8 2.1 6 2.5 4 4 3z" fill="#8dc21f"/></svg>
        855-482-7309 ext 212
      </li>
    </ul>
    <div class="divider"></div>
    <ul class="contact-list reach">
      <li>
        <svg viewBox="0 0 20 22" aria-hidden="true"><rect x="1" y="5" width="18" height="13" fill="#8dc21f"/><path d="M1 5l9 7 9-7" fill="none" stroke="#121212" stroke-width="1.6"/></svg>
        Derek@tavopayments.com
      </li>
      <li>
        <svg viewBox="0 0 20 22" aria-hidden="true"><path d="M10 1a7 7 0 0 1 7 7c0 5-7 13-7 13S3 13 3 8a7 7 0 0 1 7-7z" fill="none" stroke="#8dc21f" stroke-width="2.2"/><circle cx="10" cy="8" r="2.4" fill="#8dc21f"/></svg>
        <span>47615 Birch Hollow Rd.<br>Cedar Grove Or 91384</span>
      </li>
    </ul>
  </section>

  <section class="card card-back" aria-label="Business card back">
    <div class="brand-name faint">Tavo Payments</div>
  </section>
</main>
</body>
</html>
```